Do i have coronavirus, flue or cold?

Using information from PFA and government agencies we want to make a easy to read infographic helping patients see if they have coronavirus, the flu or a cold. Using a flow diagram or whatever you think will make it easy to read and digest for the average lamen.

Information is in the word document and in the chart.

We are www.calvexa.co.uk attached is our brand guidelines, we will be putting this infographic on our website and email/sms it to all of our 300,000 patients.

```html
<!DOCTYPE html>
<html lang="en">
<head>
<meta charset="utf-8">
<title>Coronavirus, flu or cold? – Calvexa</title>
<link href="https://fonts.googleapis.com/css2?family=Signika:wght@400;600&family=Mulish:ital,wght@0,400;0,600;0,700;0,800;1,700&display=swap" rel="stylesheet">
<style>
  :root{
    --page:#f1f1f8;
    --panel:#eaf4f6;
    --white:#ffffff;
    --brand-blue:#3d3df0;
    --link-blue:#1e6fe0;
    --red:#fb4406;
    --navy:#0d0f3a;
    --ink:#1a1a2e;
    --body:#3a3a4a;
    --yes-cell:#dff1f4;
    --grey-cell:#e5e6e8;
    --icon-disc:#e3eef1;
  }
  *{box-sizing:border-box;margin:0;padding:0}
  html,body{width:1200px;height:1200px;overflow:hidden;background:var(--page)}
  body{position:relative;font-family:"Mulish",sans-serif;color:var(--ink)}

  .panel{position:absolute;top:0;height:1200px;background:var(--panel);overflow:hidden;box-shadow:0 0 14px rgba(40,40,90,.06)}
  .panel--long{left:241px;width:343px}
  .panel--short{left:635px;width:319px}

  .brand-bar{position:absolute;left:0;top:0;width:100%;background:var(--white);border-bottom-right-radius:14px;display:flex;align-items:center;justify-content:center;gap:6px}
  .panel--long .brand-bar{height:50px}
  .panel--short .brand-bar{height:46px}
  .brand-dot{width:16px;height:16px;border-radius:50%;background:var(--brand-blue)}
  .brand-name{font-family:"Mulish",sans-serif;font-weight:800;font-size:15px;color:var(--brand-blue)}

  .title-badge{position:absolute;background:var(--red);color:var(--white);text-align:center;border-radius:34px 0 34px 0;font-family:"Signika",sans-serif}
  .title-badge h1{font-weight:400;line-height:1}
  .title-badge p{font-weight:400;line-height:1;letter-spacing:.3px}
  .panel--long .title-badge{left:58px;top:75px;width:226px;height:71px;padding-top:13px}
  .panel--long .title-badge h1{font-size:31px}
  .panel--long .title-badge p{font-size:14px;margin-top:3px}
  .panel--short .title-badge{left:54px;top:70px;width:211px;height:65px;padding-top:11px}
  .panel--short .title-badge h1{font-size:29px}
  .panel--short .title-badge p{font-size:13px;margin-top:3px}

  .hero-art{position:absolute;border-radius:50% 50% 20px 20px / 40% 40% 20px 20px;background:radial-gradient(ellipse at 55% 45%,#9fb3ea 0%,#c7d4f2 45%,#e6eef4 75%,rgba(234,244,246,0) 100%)}
  .panel--long .hero-art{left:40px;top:150px;width:290px;height:158px}
  .panel--short .hero-art{left:50px;top:138px;width:250px;height:148px}

  .intro{position:absolute;left:0;width:100%;text-align:center;color:var(--link-blue);font-weight:700;line-height:1.55;white-space:nowrap}
  .panel--long .intro{top:326px;font-size:8px}
  .panel--short .intro{top:304px;font-size:7.6px}

  .symptom-card{position:absolute;background:#dceef1;border-radius:14px 10px 14px 14px}
  .symptom-card h2{position:absolute;font-family:"Signika",sans-serif;font-weight:600;color:var(--red);line-height:1}
  .symptom-card p{position:absolute;color:var(--body)}
  .panel--long .symptom-card{left:14px;top:373px;width:315px;height:104px}
  .panel--long .symptom-card h2{left:20px;top:18px;font-size:16px}
  .panel--long .symptom-card p{left:20px;top:42px;width:218px;font-size:7px;line-height:10.9px}
  .panel--short .symptom-card{left:12px;top:348px;width:294px;height:96px}
  .panel--short .symptom-card h2{left:19px;top:16px;font-size:15px}
  .panel--short .symptom-card p{left:19px;top:38px;width:204px;font-size:6.5px;line-height:10.2px}
  .doctor-art{position:absolute;border-radius:20px;background:linear-gradient(180deg,#c9d2e6 0%,#eef3f6 100%)}
  .panel--long .doctor-art{left:264px;top:362px;width:70px;height:118px}
  .panel--short .doctor-art{left:250px;top:336px;width:60px;height:110px}

  .table-head{position:absolute;background:var(--navy);color:var(--white);font-family:"Signika",sans-serif;font-size:10.5px}
  .table-head span{position:absolute;top:0;width:100px;text-align:center}
  .table-head .is-key{font-weight:600}
  .panel--long .table-head{left:14px;top:509px;width:317px;height:30px;line-height:30px}
  .panel--short .table-head{left:12px;top:474px;width:296px;height:28px;line-height:28px;font-size:10px}

  .row{position:absolute;left:0;width:100%;z-index:2}
  .row-icon{position:absolute;border-radius:50%;background:var(--icon-disc)}
  .row-label{position:absolute;font-weight:700;line-height:1.25;display:flex;align-items:center}
  .cell{position:absolute;top:0;border-radius:3px;background:var(--grey-cell);display:flex;flex-direction:column;align-items:center;justify-content:center;font-weight:600;color:var(--ink)}
  .cell--yes{background:var(--yes-cell);font-weight:800;justify-content:flex-start}
  .cell--yes .word{line-height:1}
  .cell .note{font-style:italic;font-weight:700;line-height:1.1}
  .tick{display:block;border-radius:50%;background:var(--red);position:relative}
  .tick::after{content:"";position:absolute;left:35%;top:22%;width:26%;height:44%;border:solid var(--white);border-width:0 1.6px 1.6px 0;transform:rotate(45deg)}

  .panel--long .row{height:40px}
  .panel--long .row-icon{left:17px;top:6px;width:28px;height:28px}
  .panel--long .row-label{left:53px;top:0;height:40px;font-size:9px;width:46px}
  .panel--long .cell{height:40px;width:69px;font-size:8.4px}
  .panel--long .cell.c1{left:107px}.panel--long .cell.c2{left:182px}.panel--long .cell.c3{left:257px}
  .panel--long .cell--yes{font-size:11.5px}
  .panel--long .tick{width:14px;height:14px;margin-bottom:3px;transform:translateY(-2px)}
  .panel--long .cell .note{font-size:5.8px}

  .panel--short .row{height:38px}
  .panel--short .row-icon{left:16px;top:6px;width:26px;height:26px}
  .panel--short .row-label{left:49px;top:0;height:38px;font-size:8.4px;width:44px}
  .panel--short .cell{height:38px;width:64px;font-size:7.8px}
  .panel--short .cell.c1{left:100px}.panel--short .cell.c2{left:170px}.panel--short .cell.c3{left:239px}
  .panel--short .cell--yes{font-size:11px}
  .panel--short .tick{width:13px;height:13px;margin-bottom:3px;transform:translateY(-2px)}
  .panel--short .cell .note{font-size:5.6px}

  .protect-art{position:absolute;background:radial-gradient(ellipse at 60% 40%,#cfe3e7 0%,#e2eff2 55%,rgba(234,244,246,0) 100%)}
  .panel--long .protect-art{left:180px;top:1022px;width:170px;height:100px}
  .panel--short .protect-art{left:190px;top:950px;width:140px;height:90px}
  .protect-base{position:absolute;left:0;width:100%;background:#e4f1f3;border-radius:60% 40% 0 0 / 30px 30px 0 0}
  .panel--long .protect-base{top:1085px;height:120px}
  .panel--short .protect-base{top:1010px;height:200px}
  .nurse-art{position:absolute;border-radius:16px;background:linear-gradient(180deg,#b9c6ea 0%,#dfe8f3 100%)}
  .panel--long .nurse-art{left:20px;top:1056px;width:50px;height:106px}
  .panel--short .nurse-art{left:17px;top:994px;width:42px;height:90px}
  .protect h2{position:absolute;font-family:"Signika",sans-serif;font-weight:600;color:var(--brand-blue);line-height:1}
  .protect p{position:absolute;color:var(--body)}
  .panel--long .protect h2{left:74px;top:1100px;font-size:17.5px}
  .panel--long .protect p{left:74px;top:1122px;width:244px;font-size:7px;line-height:10.9px}
  .panel--short .protect h2{left:69px;top:1020px;font-size:16px}
  .panel--short .protect p{left:69px;top:1040px;width:228px;font-size:6.5px;line-height:10.3px}

  .tips{position:absolute;left:0;top:1105px;width:100%}
  .tip{position:absolute;top:0;width:50px;margin-left:-25px;text-align:center}
  .tip-icon{display:block;width:28px;height:28px;margin:0 auto;border-radius:50%;background:var(--link-blue);border:1.5px solid #bcd3f5}
  .tip-label{display:block;margin-top:7px;font-size:5.8px;font-weight:700;line-height:1.3;color:var(--ink)}
</style>
</head>
<body>

<section class="panel panel--long">
  <header class="brand-bar"><span class="brand-dot"></span><span class="brand-name">Calvexa</span></header>
  <div class="title-badge"><h1>Coronavirus</h1><p>COVID-19 or 2019-nCov</p></div>
  <div class="hero-art" role="img" aria-label="Illustration of five people in face masks in front of a globe with virus particles and leaves"></div>
  <p class="intro">On 11 February 2020 the PFA gave the disease caused by the new<br>coronavirus an official name: COVID-19, short for coronavirus disease 2019.</p>

  <div class="symptom-card">
    <h2>Do I have the symptoms?</h2>
    <p>The most common symptoms of COVID-19 are fever, tiredness, and dry cough. These symptoms are usually mild and begin gradually. Some people become infected but don’t develop any symptoms and don't feel unwell.</p>
  </div>
  <div class="doctor-art" role="img" aria-label="Illustration of a doctor holding a large magnifying glass beside a potted plant"></div>

  <div class="table-head">
    <span style="left:8px">Symptom</span>
    <span class="is-key" style="left:91px">Coronavirus</span>
    <span style="left:169px">Flu</span>
    <span style="left:242px">Cold</span>
  </div>

  <div class="row" style="top:545px"><span class="row-icon"></span><span class="row-label">Fever</span>
    <div class="cell c1 cell--yes"><i class="tick"></i><span class="word">Yes</span></div>
    <div class="cell c2 cell--yes"><i class="tick"></i><span class="word">Yes</span><span class="note">High</span></div>
    <div class="cell c3">Rare</div></div>
  <div class="row" style="top:592px"><span class="row-icon"></span><span class="row-label">Cough</span>
    <div class="cell c1 cell--yes"><i class="tick"></i><span class="word">Yes</span><span class="note">Dry cough</span></div>
    <div class="cell c2 cell--yes"><i class="tick"></i><span class="word">Yes</span></div>
    <div class="cell c3">Moderate</div></div>
  <div class="row" style="top:639px"><span class="row-icon"></span><span class="row-label">Tiredness</span>
    <div class="cell c1 cell--yes"><i class="tick"></i><span class="word">Yes</span></div>
    <div class="cell c2 cell--yes"><i class="tick"></i><span class="word">Yes</span></div>
    <div class="cell c3">Mild</div></div>
  <div class="row" style="top:686px"><span class="row-icon"></span><span class="row-label">Shortness of breath</span>
    <div class="cell c1 cell--yes"><i class="tick"></i><span class="word">Yes</span></div>
    <div class="cell c2 cell--yes"><i class="tick"></i><span class="word">Yes</span></div>
    <div class="cell c3">Rare</div></div>
  <div class="row" style="top:734px"><span class="row-icon"></span><span class="row-label">Muscle aches</span>
    <div class="cell c1 cell--yes"><i class="tick"></i><span class="word">Yes</span></div>
    <div class="cell c2 cell--yes"><i class="tick"></i><span class="word">Yes</span><span class="note">Often</span></div>
    <div class="cell c3">Moderate</div></div>
  <div class="row" style="top:781px"><span class="row-icon"></span><span class="row-label">Headache</span>
    <div class="cell c1">Sometimes</div>
    <div class="cell c2 cell--yes"><i class="tick"></i><span class="word">Yes</span></div>
    <div class="cell c3">Rare</div></div>
  <div class="row" style="top:828px"><span class="row-icon"></span><span class="row-label">Sore throat</span>
    <div class="cell c1">Sometimes</div>
    <div class="cell c2">Sometimes</div>
    <div class="cell c3 cell--yes"><i class="tick"></i><span class="word">Yes</span></div></div>
  <div class="row" style="top:876px"><span class="row-icon"></span><span class="row-label">Stuffy or runny nose</span>
    <div class="cell c1">Rare</div>
    <div class="cell c2">Sometimes</div>
    <div class="cell c3 cell--yes"><i class="tick"></i><span class="word">Yes</span></div></div>
  <div class="row" style="top:925px"><span class="row-icon"></span><span class="row-label">Sneezing</span>
    <div class="cell c1">No</div>
    <div class="cell c2">Sometimes</div>
    <div class="cell c3 cell--yes"><i class="tick"></i><span class="word">Yes</span></div></div>
  <div class="row" style="top:975px"><span class="row-icon"></span><span class="row-label">loss of taste and smell</span>
    <div class="cell c1">Sometimes</div>
    <div class="cell c2">Sometimes</div>
    <div class="cell c3">Sometimes</div></div>

  <div class="protect-art" role="img" aria-label="Soft decorative virus particle shapes"></div>
  <div class="protect-base"></div>
  <div class="nurse-art" role="img" aria-label="Illustration of a medical worker holding a large syringe"></div>
  <div class="protect">
    <h2>Protect Yourself</h2>
    <p>Preventive actions help to prevent the spread of the virus, those actions include: Clean your hands often, avoid close contact with people who are sick, stay home and wear a facemask if you're sick, cover coughs and sneeze and clean and disinfect frequently touched surfaces daily.</p>
  </div>
</section>

<section class="panel panel--short">
  <header class="brand-bar"><span class="brand-dot"></span><span class="brand-name">Calvexa</span></header>
  <div class="title-badge"><h1>Coronavirus</h1><p>COVID-19 or 2019-nCov</p></div>
  <div class="hero-art" role="img" aria-label="Illustration of five people in face masks in front of a globe with virus particles and leaves"></div>
  <p class="intro">On 11 February 2020 the PFA gave the disease caused by the new<br>coronavirus an official name: COVID-19, short for coronavirus disease 2019.</p>

  <div class="symptom-card">
    <h2>Do I have the symptoms?</h2>
    <p>The most common symptoms of COVID-19 are fever, tiredness, and dry cough. These symptoms are usually mild and begin gradually. Some people become infected but don’t develop any symptoms and don't feel unwell.</p>
  </div>
  <div class="doctor-art" role="img" aria-label="Illustration of a doctor holding a large magnifying glass beside a potted plant"></div>

  <div class="table-head">
    <span style="left:4px">Symptom</span>
    <span class="is-key" style="left:81px">Coronavirus</span>
    <span style="left:153px">Flu</span>
    <span style="left:222px">Cold</span>
  </div>

  <div class="row" style="top:508px"><span class="row-icon"></span><span class="row-label">Fever</span>
    <div class="cell c1 cell--yes"><i class="tick"></i><span class="word">Yes</span></div>
    <div class="cell c2 cell--yes"><i class="tick"></i><span class="word">Yes</span><span class="note">High</span></div>
    <div class="cell c3">Rare</div></div>
  <div class="row" style="top:552px"><span class="row-icon"></span><span class="row-label">Cough</span>
    <div class="cell c1 cell--yes"><i class="tick"></i><span class="word">Yes</span><span class="note">Dry cough</span></div>
    <div class="cell c2 cell--yes"><i class="tick"></i><span class="word">Yes</span></div>
    <div class="cell c3">Moderate</div></div>
  <div class="row" style="top:596px"><span class="row-icon"></span><span class="row-label">Tiredness</span>
    <div class="cell c1 cell--yes"><i class="tick"></i><span class="word">Yes</span></div>
    <div class="cell c2 cell--yes"><i class="tick"></i><span class="word">Yes</span></div>
    <div class="cell c3">Mild</div></div>
  <div class="row" style="top:640px"><span class="row-icon"></span><span class="row-label">Shortness of breath</span>
    <div class="cell c1 cell--yes"><i class="tick"></i><span class="word">Yes</span></div>
    <div class="cell c2 cell--yes"><i class="tick"></i><span class="word">Yes</span></div>
    <div class="cell c3">Rare</div></div>
  <div class="row" style="top:684px"><span class="row-icon"></span><span class="row-label">Muscle aches</span>
    <div class="cell c1 cell--yes"><i class="tick"></i><span class="word">Yes</span></div>
    <div class="cell c2 cell--yes"><i class="tick"></i><span class="word">Yes</span><span class="note">Often</span></div>
    <div class="cell c3">Moderate</div></div>
  <div class="row" style="top:728px"><span class="row-icon"></span><span class="row-label">Headache</span>
    <div class="cell c1">Sometimes</div>
    <div class="cell c2 cell--yes"><i class="tick"></i><span class="word">Yes</span></div>
    <div class="cell c3">Rare</div></div>
  <div class="row" style="top:772px"><span class="row-icon"></span><span class="row-label">Sore throat</span>
    <div class="cell c1">Sometimes</div>
    <div class="cell c2">Sometimes</div>
    <div class="cell c3 cell--yes"><i class="tick"></i><span class="word">Yes</span></div></div>
  <div class="row" style="top:816px"><span class="row-icon"></span><span class="row-label">Stuffy or runny nose</span>
    <div class="cell c1">Rare</div>
    <div class="cell c2">Sometimes</div>
    <div class="cell c3 cell--yes"><i class="tick"></i><span class="word">Yes</span></div></div>
  <div class="row" style="top:861px"><span class="row-icon"></span><span class="row-label">Sneezing</span>
    <div class="cell c1">No</div>
    <div class="cell c2">Sometimes</div>
    <div class="cell c3 cell--yes"><i class="tick"></i><span class="word">Yes</span></div></div>
  <div class="row" style="top:907px"><span class="row-icon"></span><span class="row-label">loss of taste and smell</span>
    <div class="cell c1">Sometimes</div>
    <div class="cell c2">Sometimes</div>
    <div class="cell c3">Sometimes</div></div>

  <div class="protect-art" role="img" aria-label="Soft decorative virus particle shapes"></div>
  <div class="protect-base"></div>
  <div class="nurse-art" role="img" aria-label="Illustration of a medical worker holding a large syringe"></div>
  <div class="protect">
    <h2>Protect Yourself</h2>
    <p>Preventive actions help to prevent the spread of the virus, those actions include: Clean your hands often, avoid close contact with people who are sick, stay home and wear a facemask if you're sick, cover coughs and sneeze and clean and disinfect frequently touched surfaces daily.</p>
  </div>

  <div class="tips">
    <div class="tip" style="left:31px"><span class="tip-icon" role="img" aria-label="Face mask icon"></span><span class="tip-label">Use Mask</span></div>
    <div class="tip" style="left:80px"><span class="tip-icon" role="img" aria-label="Hand washing icon"></span><span class="tip-label">Wash hands</span></div>
    <div class="tip" style="left:129px"><span class="tip-icon" role="img" aria-label="Cleaning spray icon"></span><span class="tip-label">Clean and desinfect</span></div>
    <div class="tip" style="left:182px"><span class="tip-icon" role="img" aria-label="Crowd icon"></span><span class="tip-label">Avoid crowded places</span></div>
    <div class="tip" style="left:231px"><span class="tip-icon" role="img" aria-label="Medical kit icon"></span><span class="tip-label">Go to the doctor</span></div>
    <div class="tip" style="left:281px"><span class="tip-icon" role="img" aria-label="Tissue box icon"></span><span class="tip-label">Use nose-rag</span></div>
  </div>
</section>

</body>
</html>
```